Sales Process

I need a card/page to hand out to my new clients that gives them an over view of our sales process start to finish. Along with 3 points that set us apart from all other competition.
The attached file is my first attempt with other ideas so give your suggestions.
Check out my website to get an idea of who we are. www.brightmeadowyards.com

```html
<!DOCTYPE html>
<html lang="en">
<head>
<meta charset="utf-8">
<title>Bright Meadow Yards – Our Process</title>
<link href="https://fonts.googleapis.com/css2?family=Poppins:wght@400;500;600;700;800&display=swap" rel="stylesheet">
<style>
  :root{
    --green:#7dc242;
    --ink:#3d3a36;
    --dark:#4a4744;
    --paper:#ffffff;
    --dash:#6b6864;
  }
  *{margin:0;padding:0;box-sizing:border-box}
  html,body{width:1200px;height:952px;overflow:hidden;background:var(--paper)}
  body{font-family:'Poppins',sans-serif;color:var(--ink)}
  .card{position:relative;width:1200px;height:952px;background:var(--paper)}
  .abs{position:absolute}
  .center{transform:translateX(-50%);text-align:center}

  .why-title{left:90px;top:50px;font-size:28px;font-weight:700}
  .why-item{left:128px;font-size:19px;line-height:25px;color:var(--ink)}
  .why-icon{left:86px;width:30px;height:30px}

  .brand{left:632px;top:96px;display:flex;align-items:center;gap:10px;transform:translateX(-50%);white-space:nowrap}
  .brand-dot{width:22px;height:22px;border-radius:50%;background:var(--green)}
  .brand-name{font-size:26px;font-weight:600;color:var(--ink)}
  .tagline{left:640px;top:170px;font-size:11px;color:var(--ink);white-space:nowrap}

  .photo{left:824px;top:0;width:376px;height:297px;
    background:linear-gradient(180deg,#9aa3a8 0%,#8a5a3a 30%,#6e4a34 50%,#a9a4a0 68%,#8c8580 82%,#4f6b34 100%)}

  .process-title{left:598px;top:342px;font-size:34px;font-weight:700;white-space:nowrap}
  .dash-line{top:371px;border-top:2px dashed var(--dash);height:0}

  .chain{left:0;top:0}

  .step-num{font-size:46px;font-weight:800;color:var(--green);line-height:1;white-space:nowrap}
  .step-text{font-size:17px;font-weight:500;line-height:23px;color:#222;white-space:nowrap}
  .dots{width:0;border-left:3px dotted #333}

  .footer-band{left:0;bottom:0;width:1200px;height:32px;background:var(--dark)}
</style>
</head>
<body>
<main class="card">

  <h2 class="abs why-title">Why Choose Us</h2>

  <svg class="abs why-icon" style="top:119px" viewBox="0 0 30 30" aria-hidden="true">
    <circle cx="15" cy="15" r="14" fill="var(--green)"/>
    <circle cx="15" cy="15" r="9" fill="none" stroke="#fff" stroke-width="2"/>
    <path d="M10.5 15.5l3 3 6-6.5" fill="none" stroke="#fff" stroke-width="2.4" stroke-linecap="round" stroke-linejoin="round"/>
  </svg>
  <p class="abs why-item" style="top:128px">Quality Landscaping Products</p>

  <svg class="abs why-icon" style="top:179px;height:38px" viewBox="0 0 30 38" aria-hidden="true">
    <circle cx="15" cy="13" r="12" fill="var(--green)"/>
    <path d="M9 22v14l6-4 6 4V22z" fill="var(--green)"/>
    <text x="15" y="18" font-family="Poppins,sans-serif" font-size="14" font-weight="700" fill="#fff" text-anchor="middle">$</text>
  </svg>
  <p class="abs why-item" style="top:191px">Competitive pricing</p>

  <svg class="abs why-icon" style="top:240px" viewBox="0 0 30 30" aria-hidden="true">
    <rect x="4" y="14" width="5" height="12" fill="var(--green)"/>
    <path d="M10 14l5-8c2 0 3 1 2.5 3L17 13h7c1.5 0 2.5 1.5 2 3l-2 9c-.3 1-1 1.5-2 1.5H10z" fill="var(--green)"/>
    <path d="M5 3l1 2 2 .3-1.5 1.4.4 2L5 7.7 3.1 8.7l.4-2L2 5.3 4 5z" fill="var(--green)"/>
    <path d="M25 1l1 2 2 .3-1.5 1.4.4 2L25 5.7l-1.9 1 .4-2L22 3.3 24 3z" fill="var(--green)"/>
  </svg>
  <p class="abs why-item" style="top:250px">Focus on customer satisfaction and<br>a high level of service</p>

  <div class="abs brand">
    <span class="brand-dot"></span>
    <span class="brand-name">Bright Meadow Yards</span>
  </div>
  <p class="abs tagline center">Creating Exceptional Outdoor Living Spaces</p>

  <div class="abs photo" role="img" aria-label="Photo of a stone paver patio with a round fire pit and chairs beside a wood-sided house at dusk"></div>

  <div class="abs dash-line" style="left:68px;width:354px"></div>
  <h2 class="abs process-title center">Our Process</h2>
  <div class="abs dash-line" style="left:748px;width:391px"></div>

  <svg class="abs chain" width="1200" height="952" viewBox="0 0 1200 952" aria-hidden="true">
    <g stroke="var(--green)" stroke-width="44" stroke-linecap="round">
      <line x1="234" y1="583" x2="419" y2="676"/>
      <line x1="419" y1="676" x2="602" y2="583"/>
      <line x1="602" y1="583" x2="786" y2="676"/>
      <line x1="786" y1="676" x2="971" y2="583"/>
    </g>
    <g fill="var(--green)">
      <circle cx="234" cy="583" r="76"/>
      <circle cx="419" cy="676" r="76"/>
      <circle cx="602" cy="583" r="76"/>
      <circle cx="786" cy="676" r="76"/>
      <circle cx="971" cy="583" r="76"/>
    </g>
    <g fill="#fff">
      <circle cx="234" cy="583" r="57"/>
      <circle cx="419" cy="676" r="57"/>
      <circle cx="602" cy="583" r="57"/>
      <circle cx="786" cy="676" r="57"/>
      <circle cx="971" cy="583" r="57"/>
    </g>

    <!-- phone -->
    <g transform="translate(234 583)">
      <path d="M-26-20c3-4 7-5 9-3l8 10c2 2 1 5-1 7l-4 3c3 7 8 12 15 15l3-4c2-2 5-3 7-1l10 8c2 2 1 6-3 9-4 4-10 5-16 2C-10 20-20 10-26-4c-2-6-2-11 0-16z" fill="var(--green)"/>
      <g fill="none" stroke="var(--dark)" stroke-width="3.5" stroke-linecap="round">
        <path d="M2-24a22 22 0 0 1 22 22"/>
        <path d="M2-15a13 13 0 0 1 13 13"/>
        <path d="M2-6a4 4 0 0 1 4 4"/>
      </g>
    </g>

    <!-- chat bubbles -->
    <g transform="translate(419 676)">
      <path d="M-28-24h34a6 6 0 0 1 6 6v16a6 6 0 0 1-6 6H-12l-10 8v-8h-6a6 6 0 0 1-6-6v-16a6 6 0 0 1 6-6z" fill="var(--green)"/>
      <path d="M14-6h14a6 6 0 0 1 6 6v16a6 6 0 0 1-6 6h-4v8l-10-8H0a6 6 0 0 1-6-6v-6h12a8 8 0 0 0 8-8z" fill="var(--dark)"/>
      <circle cx="-20" cy="-10" r="3" fill="#fff"/><circle cx="-11" cy="-10" r="3" fill="#fff"/><circle cx="-2" cy="-10" r="3" fill="#fff"/>
    </g>

    <!-- document with tick -->
    <g transform="translate(602 583)">
      <path d="M-26-30h30l12 12v42h-42z" fill="var(--dark)"/>
      <g stroke="#fff" stroke-width="3.5" stroke-linecap="round">
        <line x1="-18" y1="-16" x2="0" y2="-16"/>
        <line x1="-18" y1="-6" x2="6" y2="-6"/>
        <line x1="-18" y1="4" x2="2" y2="4"/>
        <line x1="-18" y1="14" x2="-4" y2="14"/>
      </g>
      <rect x="4" y="6" width="24" height="24" rx="3" fill="var(--green)" stroke="#fff" stroke-width="3"/>
      <path d="M10 18l4 4 8-8" fill="none" stroke="#fff" stroke-width="3" stroke-linecap="round" stroke-linejoin="round"/>
    </g>

    <!-- hard hat -->
    <g transform="translate(786 676)">
      <path d="M-28 2a28 28 0 0 1 56 0z" fill="var(--dark)"/>
      <rect x="-5" y="-28" width="10" height="18" fill="var(--green)"/>
      <rect x="-34" y="2" width="68" height="8" rx="2" fill="var(--dark)"/>
      <path d="M-22 16h44a22 22 0 0 1-44 0z" fill="var(--green)"/>
      <circle cx="0" cy="18" r="7" fill="#fff"/>
    </g>

    <!-- star -->
    <g transform="translate(971 583)">
      <path d="M0-30l9 19 21 3-15 14 4 21L0 17-19 27l4-21-15-14 21-3z" fill="var(--dark)"/>
      <path d="M-8 0l6 6 11-12" fill="none" stroke="var(--green)" stroke-width="4" stroke-linecap="round" stroke-linejoin="round"/>
    </g>
  </svg>

  <!-- Step 01 -->
  <div class="abs dots" style="left:234px;top:689px;height:26px"></div>
  <p class="abs step-num center" style="left:234px;top:730px">01</p>
  <p class="abs step-text center" style="left:234px;top:788px">Initial call.<br>Can we help?</p>

  <!-- Step 02 -->
  <p class="abs step-num center" style="left:422px;top:424px">02</p>
  <p class="abs step-text center" style="left:422px;top:478px">Site visit, Discuss,<br>Plan and Dream</p>
  <div class="abs dots" style="left:419px;top:542px;height:28px"></div>

  <!-- Step 03 -->
  <div class="abs dots" style="left:602px;top:689px;height:26px"></div>
  <p class="abs step-num center" style="left:602px;top:748px">03</p>
  <p class="abs step-text center" style="left:602px;top:807px">Design Proposal</p>

  <!-- Step 04 -->
  <p class="abs step-num center" style="left:786px;top:424px">04</p>
  <p class="abs step-text center" style="left:786px;top:478px">Installation<br>Construction</p>
  <div class="abs dots" style="left:786px;top:542px;height:28px"></div>

  <!-- Step 05 -->
  <div class="abs dots" style="left:971px;top:689px;height:26px"></div>
  <p class="abs step-num center" style="left:971px;top:740px">05</p>
  <p class="abs step-text center" style="left:974px;top:794px;font-weight:600">Compleat!<br>Kick back &amp; relay<br>with a SMILE on<br>your face</p>

  <div class="abs footer-band"></div>
</main>
</body>
</html>
```